Envelope Design - Winner can do follow-up business

- Marvuno.com is a Swiss-based online store selling business shirts and accessories for business men
- Please visit the webpage to make yourself familiar with the company. Although the text is in German, with Google translator you should be able to understand the main content.
- Our clients are mainly business men between 30 and 60 years old. Mostly with a high income working in the service industry (banking, insurance, lawyers, etc.). Sometimes there wives purchase the shirts for them ;-)
- The colors and the logo are given, as they are also used for the print materials (please see files in attachment)
- I am running several businesses and often need a talented web designer --> the winner gets substantial follow-up business
your task:
-for our company we need a new envelope design
-It should be simple and modern
-please use one of the logos in the followings.
-suprise me :)

```html
<!DOCTYPE html>
<html lang="de">
<head>
<meta charset="utf-8">
<title>Marvuno Envelope</title>
<link rel="stylesheet" href="https://fonts.googleapis.com/css2?family=Montserrat:wght@500;600&display=swap">
<style>
  :root {
    --backdrop: #2e2e30;
    --envelope-white: #f7f7f7;
    --facet-dark: #6b6b6e;
    --facet-mid: #a9a9ac;
    --facet-light: #d9d9db;
    --facet-peach: #f6ddd2;
    --facet-cream: #fbf6e6;
    --brand-gold: #e4c64e;
    --text-white: #ffffff;
  }
  * { margin: 0; padding: 0; box-sizing: border-box; }
  html, body {
    width: 1200px;
    height: 901px;
    overflow: hidden;
    background: var(--backdrop);
  }
  .canvas {
    position: relative;
    width: 1200px;
    height: 901px;
  }
  .envelope {
    position: absolute;
    left: 144px;
    top: 222px;
    width: 912px;
    height: 456px;
    background: var(--envelope-white);
    overflow: hidden;
  }
  .envelope__pattern {
    position: absolute;
    inset: 0;
    width: 100%;
    height: 100%;
  }
  .sender {
    position: absolute;
    left: 0;
    top: 108px;
    width: 374px;
    text-align: center;
    font-family: "Montserrat", sans-serif;
    color: var(--text-white);
  }
  .sender__name {
    font-size: 42px;
    font-weight: 500;
    letter-spacing: 3px;
    color: var(--brand-gold);
    line-height: 1;
  }
  .sender__address {
    margin-top: 30px;
    font-size: 13px;
    font-weight: 500;
    line-height: 17px;
  }
  .sender__web {
    margin-top: 20px;
    font-size: 13px;
    font-weight: 600;
  }
</style>
</head>
<body>
<div class="canvas">
  <div class="envelope">
    <svg class="envelope__pattern" viewBox="0 0 912 456" preserveAspectRatio="none" role="img" aria-label="Low-poly geometric background in grey, peach and cream tones fading to white">
      <defs>
        <linearGradient id="facet-fade" x1="0" y1="0" x2="1" y2="0.15">
          <stop offset="0" stop-color="var(--facet-dark)"/>
          <stop offset="0.28" stop-color="var(--facet-mid)"/>
          <stop offset="0.42" stop-color="var(--facet-light)"/>
          <stop offset="0.5" stop-color="var(--facet-peach)"/>
          <stop offset="0.58" stop-color="var(--facet-cream)"/>
          <stop offset="0.75" stop-color="#f1f1f1"/>
          <stop offset="1" stop-color="var(--envelope-white)"/>
        </linearGradient>
      </defs>
      <rect width="912" height="456" fill="url(#facet-fade)"/>
    </svg>
    <div class="sender">
      <div class="sender__name">MARVUNO</div>
      <p class="sender__address">Marvuno GmbH | Lindenweg 21<br>8805 Richterswil</p>
      <p class="sender__web">www.marvuno.com</p>
    </div>
  </div>
</div>
</body>
</html>
```